Design a product reviews website

We need a website design and simple logo for the brand Pivlo.com. The website will provide reviews of technology products and services. The brand and website should be approachable but should also be trustworthy and high quality. The deliverable should be designs, specs and assets that I can provide to a development team to build the website.

Target Market(s)

People researching products to buy.

Industry/Entity Type

Product

Logo Text

Pivlo.com

Number of Pages Required

5+ page

Font styles to use
Sans Serif

Colors
0492cd
0355a3
3176b5
33a6d7
85cae6
85abd2
cedeed
cee9f5

Requirements
Must have
• - Designs for the Homepage, Category and Article pages.
• - Designs for web and mobile.
• - Designs details for the engineering team to use for development.
• - I'm open to other colors than the preferences I chose but I'm more likely to like blues, greys and blacks.

```html
<!DOCTYPE html>
<html lang="en">
<head>
<meta charset="utf-8">
<title>Pivlo.com – Product &amp; Services Reviews</title>
<link rel="stylesheet" href="https://fonts.googleapis.com/css2?family=Open+Sans:wght@400;600;700&display=swap">
<style>
  :root {
    --brand: #0492cd;
    --brand-dark: #0355a3;
    --ink: #2b2b2b;
    --ink-soft: #6d6d6d;
    --rail: #f1f1f1;
    --line: #dcdcdc;
    --footer: #333333;
    --white: #ffffff;
  }
  * { box-sizing: border-box; margin: 0; padding: 0; }
  html, body { width: 830px; height: 1200px; overflow: hidden; }
  body { position: relative; background: var(--white); font-family: "Open Sans", sans-serif; color: var(--ink); }

  .site-header { position: absolute; left: 0; top: 0; width: 830px; height: 54px; background: var(--white); box-shadow: 0 1px 0 #e6e6e6; }
  .menu-toggle { position: absolute; left: 24px; top: 20px; width: 18px; }
  .menu-toggle span { display: block; height: 3px; background: #555; margin-bottom: 3px; border-radius: 1px; }
  .brand { position: absolute; left: 55px; top: 11px; display: flex; align-items: center; gap: 7px; }
  .brand-mark { width: 30px; height: 30px; border-radius: 50%; background: var(--brand); }
  .brand-name { font-size: 25px; font-weight: 700; color: var(--brand-dark); letter-spacing: 0.2px; line-height: 30px; }
  .search { position: absolute; left: 290px; top: 10px; width: 485px; height: 32px; border: 1px solid var(--line); }
  .search-button { position: absolute; right: -1px; top: -1px; width: 99px; height: 32px; background: var(--brand); color: var(--white);
    font-size: 12px; font-weight: 700; letter-spacing: 0.8px; display: flex; align-items: center; justify-content: center; gap: 6px; }

  .hero { position: absolute; left: 0; top: 54px; width: 830px; height: 231px;
    background: linear-gradient(115deg, #2c3a4b 0%, #44566a 30%, #5d6f83 55%, #7a8a9b 78%, #a4b0bc 100%); }
  .hero-title { position: absolute; left: 0; top: 80px; width: 872px; text-align: center; color: var(--white); font-size: 44px; font-weight: 700; line-height: 60px; }
  .hero-tagline { position: absolute; left: 0; top: 144px; width: 868px; text-align: center; color: var(--white); font-size: 16px; letter-spacing: 0.3px; }

  .rail-left { position: absolute; left: 0; top: 285px; width: 190px; height: 829px; background: var(--rail); }
  .rail-right { position: absolute; left: 606px; top: 285px; width: 224px; height: 829px; background: var(--rail); }

  .category-nav { position: absolute; left: 24px; top: 345px; width: 157px; list-style: none; }
  .category-nav li { height: 31px; display: flex; align-items: center; gap: 10px; padding-left: 9px; border-bottom: 1px solid var(--line);
    font-size: 9.6px; font-weight: 600; letter-spacing: 0.3px; color: #333; }
  .category-nav li.active { background: var(--brand-dark); color: var(--white); border-bottom-color: var(--brand-dark); }
  .category-nav svg { width: 13px; height: 13px; flex: none; }

  .section-title { position: absolute; font-size: 18px; font-weight: 600; color: #333; }
  .photo { position: absolute; }
  .tag { position: absolute; height: 19px; padding: 0 12px; font-size: 11px; color: var(--white); display: flex; align-items: center; border-radius: 1px; }
  .tag.light { background: var(--brand); }
  .tag.dark { background: var(--brand-dark); }
  .card-title { position: absolute; font-size: 12px; font-weight: 600; letter-spacing: 0.5px; line-height: 16.5px; text-transform: uppercase; color: #222; }
  .meta { position: absolute; display: flex; align-items: center; gap: 5px; font-size: 9.6px; color: var(--ink-soft); }
  .avatar { width: 14px; height: 14px; border-radius: 50%; background: #8a6a55; }
  .meta svg { margin-left: 9px; }

  .site-footer { position: absolute; left: 0; top: 1138px; width: 830px; height: 62px; background: var(--footer); color: #c9c9c9;
    font-size: 9.6px; letter-spacing: 0.4px; display: flex; align-items: center; justify-content: center; }
</style>
</head>
<body>
  <header class="site-header">
    <div class="menu-toggle"><span></span><span></span><span></span></div>
    <div class="brand"><div class="brand-mark"></div><div class="brand-name">Pivlo.com</div></div>
    <div class="search">
      <div class="search-button">
        <svg width="13" height="13" viewBox="0 0 13 13"><circle cx="5.5" cy="5.5" r="4.2" fill="none" stroke="#fff" stroke-width="1.8"/><line x1="8.6" y1="8.6" x2="12" y2="12" stroke="#fff" stroke-width="1.8"/></svg>
        SEARCH
      </div>
    </div>
  </header>

  <section class="hero" role="img" aria-label="Dark blue-toned photo of a businessman holding a phone at a desk">
    <h1 class="hero-title">Pivlo.com</h1>
    <p class="hero-tagline">THE BEST PRODUCT &amp; SERVICES REVIEWS &amp; RANKINGS</p>
  </section>

  <aside class="rail-left"></aside>
  <ul class="category-nav">
    <li class="active"><svg viewBox="0 0 13 13"><path d="M1 6.5 6.5 1.5 12 6.5M3 5.5V12h2.8V8.5h1.4V12H10V5.5" fill="#fff"/></svg>HOME</li>
    <li><svg viewBox="0 0 13 13"><circle cx="6.5" cy="6.5" r="5" fill="none" stroke="#444" stroke-width="1.2"/><circle cx="6.5" cy="6.5" r="1.5" fill="#444"/></svg>APPLIANCES</li>
    <li><svg viewBox="0 0 13 13"><rect x="1" y="2" width="11" height="7.5" fill="none" stroke="#444" stroke-width="1.2"/><rect x="4" y="10.5" width="5" height="1.3" fill="#444"/></svg>COMPUTER</li>
    <li><svg viewBox="0 0 13 13"><rect x="1" y="4" width="6" height="8" fill="none" stroke="#444" stroke-width="1.2"/><rect x="6" y="1" width="6" height="6" fill="none" stroke="#444" stroke-width="1.2"/></svg>ELECTRONICS</li>
    <li><svg viewBox="0 0 13 13"><circle cx="5" cy="5" r="3.5" fill="#444"/><line x1="7" y1="7" x2="12" y2="12" stroke="#444" stroke-width="2"/></svg>HOME SECURITY</li>
    <li><svg viewBox="0 0 13 13"><rect x="3" y="0.8" width="7" height="11.4" rx="1" fill="none" stroke="#444" stroke-width="1.2"/></svg>MOBILE</li>
    <li><svg viewBox="0 0 13 13"><path d="M1 6.5 6.5 1.5 12 6.5M3 5.5V12h7V5.5" fill="none" stroke="#444" stroke-width="1.2"/></svg>SMART HOME</li>
    <li><svg viewBox="0 0 13 13"><circle cx="6.5" cy="6" r="4.5" fill="none" stroke="#444" stroke-width="1.2"/><rect x="4.5" y="10" width="4" height="2.5" fill="#444"/></svg>SOFTWARE</li>
  </ul>

  <main>
    <h2 class="section-title" style="left:206px;top:303px;">New</h2>

    <div class="photo" style="left:206px;top:344px;width:381px;height:252px;background:linear-gradient(180deg,#f4f4f2 0%,#e4e4e1 38%,#c9c7c1 62%,#9d8a74 82%,#5d4a3a 100%);" role="img" aria-label="Bright white living room with a smart speaker on a windowsill"></div>
    <span class="tag light" style="left:450px;top:567px;">Home</span>
    <span class="tag dark" style="left:514px;top:567px;">Speaker</span>
    <h3 class="card-title" style="left:206px;top:612px;">The Vora Hub... one of our essentials</h3>
    <div class="meta" style="left:207px;top:634px;"><span class="avatar"></span>Marcus Reed
      <svg width="10" height="10" viewBox="0 0 10 10"><circle cx="5" cy="5" r="4.2" fill="none" stroke="#555" stroke-width="1"/><path d="M5 2.5V5h2" fill="none" stroke="#555" stroke-width="1"/></svg>July 18,2016</div>

    <div class="photo" style="left:206px;top:676px;width:180px;height:136px;background:linear-gradient(175deg,#a85a2a 0%,#c98a55 22%,#efe9e2 48%,#8f9a7a 74%,#f1efec 100%);" role="img" aria-label="Copper pots and herbs hanging on a kitchen rail"></div>
    <span class="tag light" style="left:324px;top:785px;">Home</span>
    <h3 class="card-title" style="left:206px;top:824px;">The easiest all-in-one<br>kitchen sets</h3>

    <div class="photo" style="left:406px;top:676px;width:181px;height:136px;background:linear-gradient(180deg,#f0f0ee 0%,#dedcd8 45%,#c7b69c 68%,#9c9690 88%,#6f6b66 100%);" role="img" aria-label="White kitchen with wooden table and white chairs"></div>
    <h3 class="card-title" style="left:405px;top:824px;">The best temporary stay<br>services for long trips</h3>

    <div class="photo" style="left:206px;top:890px;width:381px;height:160px;background:linear-gradient(100deg,#3a3a3a 0%,#cfcfcc 25%,#f0f0ee 50%,#5a5856 68%,#d6d4d0 84%,#8a6a4c 100%);" role="img" aria-label="Woman working at a desk in a bright room with a bicycle"></div>
    <span class="tag dark" style="left:523px;top:1021px;">Audio</span>
    <h3 class="card-title" style="left:206px;top:1065px;">Reviews of the 6 best wireless speakers in the market</h3>
    <div class="meta" style="left:207px;top:1088px;"><span class="avatar"></span>Marcus Reed
      <svg width="10" height="10" viewBox="0 0 10 10"><circle cx="5" cy="5" r="4.2" fill="none" stroke="#555" stroke-width="1"/><path d="M5 2.5V5h2" fill="none" stroke="#555" stroke-width="1"/></svg>July 18,2016</div>
  </main>

  <aside class="rail-right"></aside>
  <h2 class="section-title" style="left:624px;top:303px;">Popular</h2>

  <div class="photo" style="left:624px;top:345px;width:180px;height:135px;background:linear-gradient(90deg,#d4d4d2 0%,#b9b8b4 30%,#5f5d5a 46%,#d9d8d5 60%,#efeeec 100%);" role="img" aria-label="Grey bedroom with framed prints and a lamp"></div>
  <h3 class="card-title" style="left:625px;top:492px;">Copper pots that won't<br>break the bank</h3>

  <div class="photo" style="left:625px;top:549px;width:180px;height:135px;background:linear-gradient(170deg,#ecece9 0%,#c9c4bc 30%,#8c6a48 55%,#d8d8d6 75%,#3a3a3a 100%);" role="img" aria-label="Kitchen with wooden dining table and white chairs"></div>
  <span class="tag light" style="left:744px;top:657px;">Home</span>
  <h3 class="card-title" style="left:626px;top:696px;">Copper pots that won't<br>break the bank</h3>

  <div class="photo" style="left:625px;top:753px;width:180px;height:135px;background:linear-gradient(180deg,#f0b81a 0%,#e3a91c 22%,#e2ded6 45%,#b7b2aa 62%,#a4622e 80%,#7a4520 100%);" role="img" aria-label="Yellow kitchen with a round table and wire chairs"></div>
  <h3 class="card-title" style="left:626px;top:900px;">Copper pots that won't<br>break the bank</h3>

  <footer class="site-footer">COPYRIGHT © 2016 PIVLO. ALL RIGHTS RESERVED</footer>
</body>
</html>
```